Larkspur Homes - wanted BRILLIANT website design for our new property investing company

We need a website design for our new company based in Bristol, England, UK called "Larkspur Homes". We help buy people property who are in financial difficulty or who are needing to sell their property quickly for reasons such as death, divorce/separation, relocation, emigration.

We have a logo being designed incorporating strawberry and property (so red and green). We would like designs to communicate an elegant ,professional, approachable, friendly
fresh clean but also warm appealing appearance
Not too busy
Website consistent with logo and company name i.e. colour scheme

Please use our word document for content as a guide but use professional judgement for minor alterations if you feel they would benefit the site/structure etc

Please ask at any time if not sure

Target Market(s)

Adult british population, those that have a mortgage / loan / own property

Industry/Entity Type

Financial

Font styles to use
Serif
Sans Serif
Decorative

Colors
0692cd
33b7a4
acd036
fbee3e
3176b5
886aae
a6479a
e567a6
eb1f27

Requirements
Must have
• This must not look like a template website we are looking for UNIQUE please!
Nice to have
• Bristol pictures instead of generic, or colourful line drawings/comic drawings of houses/property/keys/happy people.....
Should not have
• An obvious off the shelf template design

```html
<!DOCTYPE html>
<html lang="en">
<head>
<meta charset="utf-8">
<title>Larkspur Homes</title>
<link href="https://fonts.googleapis.com/css2?family=Roboto:wght@300;400;500;700&family=Roboto+Condensed:wght@700&display=swap" rel="stylesheet">
<style>
:root{
  --red:#e31e24;
  --green:#1db51d;
  --green-dark:#0f8a10;
  --ink:#333;
  --muted:#666;
  --paper:#f4f4f4;
  --dark:#1c1c1c;
  --darker:#121212;
  --line:#dcdcdc;
}
*{margin:0;padding:0;box-sizing:border-box}
html,body{width:738px;height:1200px;overflow:hidden}
body{font-family:'Roboto',sans-serif;background:var(--paper);color:var(--ink);position:relative}
.wrap{position:absolute;left:63px;right:63px}

/* header */
.site-header{position:absolute;top:0;left:0;width:738px;height:72px;background:#f7f7f7}
.brand{position:absolute;left:63px;top:24px;font-size:21px;font-weight:500;color:var(--red)}
.header-contact{position:absolute;right:63px;top:27px;text-align:right;font-size:9px;color:#555;line-height:14px}
.header-contact svg{vertical-align:-1px;margin-right:4px}

/* nav */
.main-nav{position:absolute;top:72px;left:0;width:738px;height:28px;background:linear-gradient(#27c227,#17a817)}
.main-nav ul{list-style:none;display:flex;position:absolute;left:63px;top:0;height:28px}
.main-nav li{color:#fff;font-size:10px;line-height:28px;padding:0 14px;border-right:1px solid rgba(0,0,0,.15)}
.main-nav li.active{background:var(--green-dark);padding:0 16px}
.main-nav li.active svg{vertical-align:-1px;margin-right:5px}
.main-nav li:last-child{border-right:none}

/* hero */
.hero{position:absolute;top:100px;left:0;width:738px;height:291px;background:linear-gradient(100deg,#cdc5b8 0%,#e9e2d6 35%,#b9a690 60%,#d8d2c8 85%,#bfb8ae 100%)}
.hero h1{position:absolute;top:145px;left:0;width:738px;text-align:center;font-family:'Roboto Condensed',sans-serif;font-size:27px;line-height:37px;color:#fff;text-shadow:1px 2px 2px rgba(0,0,0,.55);text-transform:uppercase}
.hero h1 em{font-style:normal;color:var(--red)}
.btn-more{position:absolute;left:310px;top:229px;width:99px;height:25px;background:var(--green);border:2px solid #fff;color:#fff;font-size:11px;font-weight:500;text-align:center;line-height:21px}

/* intro */
.intro-title{position:absolute;top:419px;left:63px;font-size:14px;color:var(--red)}
.intro-photo{position:absolute;top:447px;left:63px;width:386px;height:142px;background:linear-gradient(90deg,#e8e8e8,#f5f5f5 50%,#dcdcdc);border:1px solid #ddd}
.service-list{position:absolute;top:597px;list-style:none;font-size:8.5px;color:#555}
.service-list li{height:18.5px;line-height:18px;border-bottom:1px solid #e2e2e2;padding-left:12px;position:relative}
.service-list li::before{content:"";position:absolute;left:0;top:6px;width:5px;height:5px;border:1px solid #777;border-radius:50%}
.service-list li.hl{color:var(--green)}
.service-list li.hl::before{border-color:var(--green)}
.list-a{left:63px;width:230px}
.list-b{left:323px;width:126px}

/* contact form */
.contact-card{position:absolute;top:415px;left:496px;width:178px;height:267px;background:#fff;border:1px solid #e0e0e0}
.contact-card h2{height:31px;background:#1d1d1d;color:#fff;font-size:13px;font-weight:400;text-align:center;line-height:31px}
.field{position:absolute;left:12px;width:153px;height:23px;border:1px solid #ddd;font-size:7.5px;color:#666;padding:6px 8px}
.field.focus{border-color:var(--green)}
.field.msg{height:71px}
.btn-send{position:absolute;left:12px;top:229px;width:153px;height:23px;background:var(--green);color:#fff;font-size:12px;font-weight:500;text-align:center;line-height:23px}

/* who */
.who{position:absolute;top:725px;left:0;width:738px;height:211px;background:linear-gradient(90deg,#3a2f27,#5a4a3e 50%,#2e2621)}
.who h2{position:absolute;top:23px;width:738px;text-align:center;color:#fff;font-size:17px;font-weight:400}
.who-rule{position:absolute;top:36px;left:160px;width:418px;height:1px;background:rgba(255,255,255,.12)}
.who ol{position:absolute;top:69px;list-style:none;font-size:10px;color:#fff;font-weight:300}
.who li{height:21.4px;display:flex;align-items:center}
.who li b{display:inline-block;width:11px;height:11px;border:1px solid #fff;border-radius:50%;font-size:6.5px;font-weight:400;text-align:center;line-height:9px;margin-right:7px}
.who li.hl{color:var(--green)}
.who li.hl b{border-color:var(--green)}
.col1{left:63px}.col2{left:296px}.col3{left:527px}

/* partners */
.partners{position:absolute;top:936px;left:0;width:738px;height:69px;background:#f2f2f2}
.partners h2{position:absolute;left:63px;top:22px;font-size:19px;font-weight:300;color:var(--red)}
.partners .divider{position:absolute;left:188px;top:12px;width:1px;height:44px;background:#ddd}
.badge{position:absolute;background:#8a8a8a}

/* footer */
.site-footer{position:absolute;top:1005px;left:0;width:738px;height:165px;background:var(--dark)}
.footer-brand{position:absolute;left:65px;top:27px;width:203px;height:115px;background:#0b0b0b;color:#666;font-size:26px;font-weight:300;text-align:center;line-height:30px;padding-top:28px}
.footer-col{position:absolute;top:32px}
.footer-col h3{font-size:11px;font-weight:400;color:var(--red);margin-bottom:12px}
.footer-col ul{list-style:none;font-size:7.5px;color:#ddd}
.sitemap li{height:14.5px}
.footer-contact p{font-size:7px;color:#ddd;line-height:11px;width:150px}
.footer-contact .row{font-size:8.5px;color:#ddd;margin-top:6px;display:flex;line-height:13px}
.footer-contact .row svg{margin-right:9px;margin-top:3px;flex:none}
.social li{height:16px;display:flex;align-items:center;font-size:8px}
.social li i{display:inline-block;width:11px;height:11px;margin-right:7px}
.copyright{position:absolute;top:1170px;left:0;width:738px;height:30px;background:var(--darker);color:#fff;font-size:7.5px;text-align:center;line-height:30px}
</style>
</head>
<body>

<header class="site-header">
  <div class="brand">Larkspur Homes</div>
  <div class="header-contact">
    <div><svg width="8" height="8" viewBox="0 0 10 10"><path d="M2 0l2 2-1 2 3 3 2-1 2 2-2 2C4 10 0 6 0 2z" fill="#555"/></svg>0117 - 4960 - 382</div>
    <div><svg width="9" height="7" viewBox="0 0 10 7"><rect width="10" height="7" fill="#666"/><path d="M0 0l5 4 5-4" stroke="#f7f7f7" fill="none"/></svg>info@larkspur-homes.co.uk</div>
  </div>
</header>

<nav class="main-nav">
  <ul>
    <li class="active"><svg width="9" height="8" viewBox="0 0 10 9"><path d="M5 0l5 4.5H8.5V9H6V6H4v3H1.5V4.5H0z" fill="#fff"/></svg>Home</li>
    <li>Sell Your Property Fast</li>
    <li>Rent Your Property Fast</li>
    <li>The 5 Easy Steps</li>
    <li>About us</li>
    <li>Contact us</li>
  </ul>
</nav>

<section class="hero" role="img" aria-label="Bright modern living room with sofas, fireplace and television">
  <h1>Do you want to <em>sell</em> or <em>rent</em> out your<br>house quickly?</h1>
  <div class="btn-more">Read More &#8857;</div>
</section>

<h2 class="intro-title">We are a local family run property business who specialize in</h2>
<div class="intro-photo" role="img" aria-label="Business team with a hand holding a small model house"></div>
<ul class="service-list list-a">
  <li>Buying properties quickly</li>
  <li class="hl">Finding creative solutions to your property problems</li>
  <li>Property rental management</li>
  <li>Lettings to professional and student tenants</li>
  <li>Guaranteed rent and management schemes for</li>
</ul>
<ul class="service-list list-b">
  <li>landlords</li>
  <li>STOPPING repossessions</li>
  <li>Motivated sellers</li>
  <li>Chain fixing</li>
  <li>Negative equity problems</li>
</ul>

<aside class="contact-card">
  <h2>Contact Form</h2>
  <div class="field" style="top:43px">Name</div>
  <div class="field" style="top:70px">Email</div>
  <div class="field" style="top:97px">Phone number</div>
  <div class="field focus" style="top:125px">Property address</div>
  <div class="field msg" style="top:153px">Message</div>
  <div class="btn-send">Send</div>
</aside>

<section class="who" role="img" aria-label="Softly blurred bedroom interior">
  <div class="who-rule"></div>
  <h2><span style="background:transparent;padding:0 10px">Who can we help</span></h2>
  <ol class="col1">
    <li><b>1</b>How to stop repossession</li>
    <li><b>2</b>Divorce or separation</li>
    <li><b>3</b>Financial problems</li>
    <li><b>4</b>Don't like estate agents?</li>
    <li><b>5</b>Property needing work</li>
  </ol>
  <ol class="col2">
    <li><b>6</b>Retiring landlords</li>
    <li class="hl"><b>7</b>Negative equity</li>
    <li><b>8</b>Opportunity not to be missed!!</li>
    <li><b>9</b>Guaranteed rent scheme</li>
    <li><b>10</b>Ill health</li>
  </ol>
  <ol class="col3">
    <li><b>11</b>Retiring landlords</li>
    <li><b>12</b>Negative equity</li>
    <li><b>13</b>Opportunity not to be missed!!</li>
    <li><b>14</b>Guaranteed rent scheme</li>
    <li><b>15</b>Ill health</li>
  </ol>
</section>

<section class="partners">
  <h2>Our Partners</h2>
  <div class="divider"></div>
  <div class="badge" style="left:227px;top:16px;width:104px;height:36px;border-radius:4px"></div>
  <div class="badge" style="left:363px;top:16px;width:106px;height:36px;background:#1f3f7a"></div>
  <div class="badge" style="left:506px;top:14px;width:28px;height:38px"></div>
  <div class="badge" style="left:565px;top:16px;width:104px;height:36px;border-radius:4px"></div>
</section>

<footer class="site-footer">
  <div class="footer-brand">Larkspur<br>Homes</div>
  <div class="footer-col sitemap" style="left:302px">
    <h3>Sitemap</h3>
    <ul>
      <li>Home</li>
      <li>Sell Your Property Fast</li>
      <li>Rent Your Property Fast</li>
      <li>The 5 Easy Steps</li>
      <li>About us</li>
      <li>Contact us</li>
    </ul>
  </div>
  <div class="footer-col footer-contact" style="left:434px">
    <h3>Contact us</h3>
    <p>Lorem Ipsum is simply dummy text of the printing and typesetting industry.</p>
    <div class="row"><svg width="9" height="7" viewBox="0 0 10 7"><rect width="10" height="7" fill="#888"/><path d="M0 0l5 4 5-4" stroke="#1c1c1c" fill="none"/></svg><span>info@larkspur-<br>homes.co.uk</span></div>
    <div class="row" style="margin-top:2px"><svg width="8" height="8" viewBox="0 0 10 10"><path d="M2 0l2 2-1 2 3 3 2-1 2 2-2 2C4 10 0 6 0 2z" fill="#888"/></svg><span>0117 4960382</span></div>
  </div>
  <div class="footer-col social" style="left:612px">
    <h3>Follow us</h3>
    <ul>
      <li><i style="background:#3b5998"></i>Chatterbook</li>
      <li><i style="background:#2fa9e0"></i>Tweeter</li>
      <li><i style="background:#d6492f"></i>Circleplus</li>
      <li><i style="background:#0f76b0"></i>Linkwork</li>
    </ul>
  </div>
</footer>
<div class="copyright">2014 Larkspur Homes Limited. Reg No 4417026</div>

</body>
</html>
```